2 Creative Website Banners for Furniture Brand

Morning Tobrasca....
The get a great night sleep banner is complete - we are happy with that one.
Ive uploaded a slightly different concept for the other banner below. This is just something rough ive thrown together. But you can see I have added a curve, a maroon coloured background which is slightly transparent and a big heart in the background....
I do not necessarily want to use this heart image but something a bit like this (a nice graphic, gif etc) but something quite elegant faded in, or perhaps a number of hearts (done in a tasteful way). Also can we keep the typography in the same format as you can see for this one.
Nearly there :)!
Industry/Entity Type
Furniture

```html
<!DOCTYPE html>
<html lang="en">
<head>
<meta charset="utf-8">
<title>Bedroom Banners</title>
<link rel="stylesheet" href="https://fonts.googleapis.com/css2?family=Great+Vibes&family=Jost:wght@300;400&family=Marcellus&display=swap">
<style>
  :root {
    --page-bg: #9a9a9a;
    --banner-black: #0c0c0d;
    --banner-charcoal: #26262a;
    --cream: #e6dccb;
    --white: #ffffff;
    --body-text: #d9d9d9;
    --button-text: #3a3a3a;
    --room-dark: #2c2c33;
    --room-mid: #4a4a55;
    --bed-mauve: #7a6a72;
    --bed-light: #a89ba3;
  }
  * { margin: 0; padding: 0; box-sizing: border-box; }
  html, body { width: 1200px; height: 1200px; overflow: hidden; }
  body { background: var(--page-bg); position: relative; font-family: "Jost", sans-serif; }

  .banner {
    position: absolute;
    left: 61px;
    width: 1076px;
    height: 320px;
    overflow: hidden;
  }
  .banner--script { top: 239px; background: var(--banner-black); }
  .banner--serif { top: 653px; background: var(--banner-charcoal); }

  .scene-dresser {
    position: absolute;
    left: 0; top: 0;
    width: 557px; height: 100%;
    background: linear-gradient(90deg, rgba(0,0,0,0) 0%, rgba(0,0,0,0) 45%, var(--room-dark) 75%, var(--room-mid) 100%);
  }
  .scene-bedroom {
    position: absolute;
    left: 557px; top: 0;
    width: 519px; height: 100%;
    background: linear-gradient(160deg, #3a3036 0%, #5a4c54 35%, var(--bed-mauve) 60%, var(--bed-light) 80%, #8e949c 100%);
  }

  .copy { position: absolute; top: 0; left: 0; }

  .headline-script {
    position: absolute;
    left: 55px; top: 14px;
    font-family: "Great Vibes", cursive;
    font-size: 118px;
    line-height: 1;
    color: var(--cream);
    white-space: nowrap;
  }
  .tagline {
    position: absolute;
    font-weight: 300;
    font-size: 19px;
    letter-spacing: 0.3px;
    color: var(--white);
    white-space: nowrap;
  }
  .banner--script .tagline { left: 44px; top: 166px; }
  .banner--serif .tagline { left: 59px; top: 56px; }

  .headline-serif {
    position: absolute;
    left: 55px; top: 70px;
    font-family: "Marcellus", serif;
    font-size: 116px;
    line-height: 1;
    color: var(--white);
    letter-spacing: 1px;
  }
  .body-text {
    position: absolute;
    width: 186px;
    font-size: 8.5px;
    line-height: 12px;
    color: var(--body-text);
    text-align: justify;
  }
  .banner--script .body-text { left: 45px; top: 196px; }
  .banner--serif .body-text { left: 60px; top: 196px; }

  .button-pill {
    position: absolute;
    left: 46px; top: 259px;
    width: 178px; height: 27px;
    border-radius: 14px;
    background: var(--cream);
    color: var(--button-text);
    font-size: 15px;
    line-height: 27px;
    text-align: center;
    letter-spacing: 0.2px;
  }
  .button-arrow {
    position: absolute;
    left: 61px; top: 242px;
    width: 173px; height: 28px;
  }
  .button-arrow svg { position: absolute; inset: 0; }
  .button-arrow span {
    position: relative;
    display: block;
    color: var(--button-text);
    font-size: 15px;
    line-height: 28px;
    text-align: center;
    letter-spacing: 0.2px;
  }
</style>
</head>
<body>

  <section class="banner banner--script">
    <div class="scene-dresser" role="img" aria-label="Mirrored dressing table with glass jars, ornate mirror and velvet stool"></div>
    <div class="scene-bedroom" role="img" aria-label="Bedroom with upholstered headboard, mauve bedding, faux fur throw and mirrored bedside tables"></div>
    <div class="copy">
      <h1 class="headline-script">Love</h1>
      <p class="tagline">FIND A LOOK YOU</p>
      <p class="body-text">Lorem Ipsum is simply dummy text of the printing and typesetting industry.</p>
      <a class="button-pill">SHOP BEDROOMS</a>
    </div>
  </section>

  <section class="banner banner--serif">
    <div class="scene-dresser" role="img" aria-label="Mirrored dressing table with glass jars, ornate mirror and velvet stool"></div>
    <div class="scene-bedroom" role="img" aria-label="Bedroom with upholstered headboard, mauve bedding, faux fur throw and mirrored bedside tables"></div>
    <div class="copy">
      <p class="tagline">FIND A LOOK YOU</p>
      <h1 class="headline-serif">LOVE</h1>
      <p class="body-text">Lorem Ipsum is simply dummy text of the printing and typesetting industry.</p>
      <a class="button-arrow">
        <svg width="173" height="28" viewBox="0 0 173 28" aria-hidden="true">
          <polygon points="9,0 164,0 173,14 164,28 9,28 0,14" fill="#e6dccb"/>
        </svg>
        <span>SHOP BEDROOMS</span>
      </a>
    </div>
  </section>

</body>
</html>
```